Veltrona stationery design

Design stationery for us that fits with the colours of the logo. We are looking for letterheads, business cards etc. Something we can use for a prospectus and marketing presentations in power point. Must be completed in such a manner that it represents a corporate image for large enterprise clients and other large organisations. The company is a project assurance and monitoring company that works in all industries.

```html
<!DOCTYPE html>
<html lang="en">
<head>
<meta charset="UTF-8">
<title>Veltrona Business Cards</title>
<link href="https://fonts.googleapis.com/css2?family=Montserrat:wght@400;700;800&display=swap" rel="stylesheet">
<style>
  :root {
    --backdrop: #262626;
    --card: #0d0d0d;
    --blue: #1e6fe0;
    --blue-deep: #1f3f9a;
    --orange: #f2581e;
    --text: #f2f2f2;
  }
  * { margin: 0; padding: 0; box-sizing: border-box; }
  html, body { width: 1200px; height: 900px; overflow: hidden; }
  body {
    background: var(--backdrop);
    font-family: "Montserrat", sans-serif;
    position: relative;
  }
  .card {
    position: absolute;
    width: 620px;
    height: 354px;
    background: var(--card);
    border-radius: 4px;
    box-shadow: 0 18px 40px rgba(0,0,0,0.55);
    overflow: hidden;
  }
  .card--front { left: 90px; top: 90px; }
  .card--back { left: 490px; top: 456px; }

  .brand {
    display: flex;
    align-items: center;
    gap: 12px;
  }
  .brand__mark {
    width: 26px; height: 26px;
    background: var(--orange);
  }
  .brand__name {
    font-weight: 800;
    letter-spacing: 2px;
    color: var(--blue);
  }
  .card--front .brand {
    position: absolute;
    left: 50%; top: 50%;
    transform: translate(-50%, -50%);
  }
  .card--front .brand__mark { width: 38px; height: 38px; }
  .card--front .brand__name { font-size: 40px; }

  .card--back .brand {
    position: absolute;
    left: 40px; top: 106px;
  }
  .card--back .brand__name { font-size: 26px; }

  .person {
    position: absolute;
    left: 330px; top: 34px;
  }
  .person__name {
    font-size: 17px;
    font-weight: 700;
    color: var(--blue-deep);
    letter-spacing: 0.5px;
  }
  .person__title {
    font-size: 14px;
    color: var(--orange);
    text-align: right;
    margin-top: 2px;
  }

  .address {
    position: absolute;
    left: 40px; top: 196px;
    font-size: 14px;
    line-height: 1.3;
    color: var(--text);
  }
  .contacts {
    position: absolute;
    left: 40px; top: 248px;
    list-style: none;
    font-size: 14px;
    line-height: 1.5;
    color: var(--text);
  }
  .contacts li { display: flex; align-items: center; gap: 8px; }
  .contacts svg { width: 12px; height: 12px; fill: var(--orange); flex: none; }

  .corner-band {
    position: absolute;
    right: 0; top: 0;
    width: 260px; height: 354px;
  }
</style>
</head>
<body>
  <section class="card card--front">
    <div class="brand">
      <span class="brand__mark"></span>
      <span class="brand__name">VELTRONA</span>
    </div>
  </section>

  <section class="card card--back">
    <svg class="corner-band" viewBox="0 0 260 354" aria-hidden="true">
      <polygon points="260,40 260,354 120,354" fill="var(--blue-deep)"/>
      <circle cx="150" cy="170" r="70" fill="var(--blue)"/>
    </svg>

    <div class="person">
      <div class="person__name">MARISA CALDER</div>
      <div class="person__title">Director</div>
    </div>

    <div class="brand">
      <span class="brand__mark"></span>
      <span class="brand__name">VELTRONA</span>
    </div>

    <p class="address">1850 Harbor Ave<br>Suite 310 Houston</p>

    <ul class="contacts">
      <li>
        <svg viewBox="0 0 24 24"><path d="M6.6 10.8a15 15 0 0 0 6.6 6.6l2.2-2.2a1 1 0 0 1 1-.25 11.4 11.4 0 0 0 3.6.57 1 1 0 0 1 1 1V20a1 1 0 0 1-1 1A17 17 0 0 1 3 4a1 1 0 0 1 1-1h3.5a1 1 0 0 1 1 1 11.4 11.4 0 0 0 .57 3.6 1 1 0 0 1-.25 1z"/></svg>
        555-014-2290
      </li>
      <li>
        <svg viewBox="0 0 24 24"><path d="M2 5h20v14H2z M2 5l10 8 10-8" stroke="#0d0d0d" stroke-width="1.5"/></svg>
        info@veltrona.com
      </li>
      <li>
        <svg viewBox="0 0 24 24"><circle cx="12" cy="12" r="10"/></svg>
        www.veltrona.com
      </li>
    </ul>
  </section>
</body>
</html>
```